Martial Art workout site needs web page design

We need a web page designed for our new martial art web site that presents innovated, monthly workouts, done by beautiful models
Web page should include
- a home page
- Page for the monthly workout
- Gallery page for the models (pics & video)
-Archived page for past workout
- Page to sign up for monthly updates
- Sponsor Page

Martial Art

```html
<!DOCTYPE html>
<html lang="en">
<head>
<meta charset="utf-8">
<title>Reed Calloway Martial Arts</title>
<link href="https://fonts.googleapis.com/css2?family=Noticia+Text:wght@400;700&display=swap" rel="stylesheet">
<style>
:root{
  --coral:#e3604f;
  --coral-deep:#dc5258;
  --coral-light:#ec7654;
  --ink:#333333;
  --muted:#777777;
  --nav-top:#4a4a4a;
  --nav-bottom:#2e2e2e;
  --footer:#3b3b3b;
  --line:#e2e2e2;
  --white:#ffffff;
}
*{margin:0;padding:0;box-sizing:border-box}
html,body{width:976px;height:1200px;overflow:hidden;background:var(--white)}
body{font-family:"Noticia Text",Georgia,serif;color:var(--ink)}
.page{position:relative;width:976px;height:1200px;overflow:hidden}
.abs{position:absolute}

/* header */
.brand-mark{left:107px;top:24px;width:65px;height:65px;border-radius:50%;background:var(--coral);box-shadow:0 0 0 4px #f1f1f1}
.brand-name{left:183px;top:20px;font-size:40px;line-height:48px;color:#3a3a3a}
.brand-tag{left:184px;top:69px;font-size:13px;letter-spacing:4px;color:#8a8a8a}
.social{top:46px;width:27px;height:27px;border-radius:50%;background:#9a9a9a}

/* nav */
.nav{left:0;top:112px;width:976px;height:41px;background:linear-gradient(var(--nav-top),var(--nav-bottom))}
.nav ul{list-style:none;position:absolute;left:107px;top:0;height:41px;display:flex}
.nav li{height:41px;display:flex;align-items:center;justify-content:center;color:var(--white);font-size:11.5px;text-transform:uppercase;border-right:1px solid #222;box-shadow:1px 0 0 #555}
.nav li:last-child{border-right:none;box-shadow:none}

/* hero */
.hero{left:0;top:153px;width:976px;height:410px;background:radial-gradient(ellipse at 45% 45%,var(--coral-light) 0%,var(--coral) 55%,var(--coral-deep) 100%)}
.hero-photo{left:110px;top:22px;width:420px;height:362px;border-radius:40% 50% 45% 40%;background:radial-gradient(ellipse at center,#f4eee9 0%,#eadfd8 50%,rgba(234,112,84,0) 72%)}
.hero-title{left:569px;top:80px;color:var(--white);font-size:42px;line-height:54px;text-transform:uppercase;width:360px}
.hero-text{left:571px;top:200px;width:290px;color:var(--white);font-size:12px;line-height:20px}
.hero-btn{left:572px;top:294px;width:147px;height:32px;background:linear-gradient(#444,#262626);color:var(--white);font-size:12px;display:flex;align-items:center;justify-content:center}
.hero-arrow{top:187px;width:31px;height:31px}

/* content */
.welcome-title{left:107px;top:600px;font-size:21px;color:#333}
.welcome-lead{left:107px;top:641px;width:245px;font-size:10.6px;line-height:19.5px;text-transform:uppercase;color:#333}
.welcome-body{left:107px;top:688px;width:245px;font-size:11px;line-height:16.4px;color:var(--muted)}
.read-more{left:107px;top:808px;font-size:11.5px;color:var(--coral);display:flex;align-items:center;gap:6px}

.video-title{left:367px;top:604px;font-size:17px;color:var(--coral)}
.video-frame{left:367px;top:642px;width:243px;height:141px;background:linear-gradient(90deg,#d9d6d2 0%,#b4a79c 45%,#a9906f 75%,#c9b8a8 100%)}
.play{left:461px;top:683px;width:58px;height:58px}
.video-caption{left:367px;top:797px;width:243px;font-size:11px;line-height:16.4px;color:var(--muted)}

.signup{left:629px;top:602px;width:240px;height:221px;border:1px solid var(--coral)}
.signup-head{left:0;top:0;width:238px;height:35px;background:var(--coral);color:var(--white);font-size:15.5px;padding:8px 0 0 12px}
.field{left:9px;width:179px;height:26px;border:1px solid #dcdcdc;border-radius:2px;background:linear-gradient(#f9f9f9,#fff);font-size:9.5px;font-style:italic;color:#999;padding:7px 0 0 13px}
.signup-btn{left:147px;top:183px;width:79px;height:24px;background:linear-gradient(#444,#222);color:var(--white);font-size:11px;display:flex;align-items:center;justify-content:center}

/* gallery */
.gallery{left:0;top:885px;width:976px;height:197px;background:linear-gradient(#f7f7f7,#fcfcfc);border-top:1px solid #ececec;border-bottom:1px solid #ececec}
.gallery-title{left:107px;top:13px;font-size:21px;color:var(--coral)}
.gallery-next{left:847px;top:15px;width:23px;height:23px}
.thumb{top:52px;height:117px;background:var(--white);padding:3px;box-shadow:0 0 3px rgba(0,0,0,.18)}
.thumb div{width:100%;height:100%}

/* footer */
.footer{left:0;top:1120px;width:976px;height:80px;background:var(--footer)}
.footer-copy{left:110px;top:17px;font-size:11px;line-height:20.5px;color:var(--white)}
.footer-copy span{color:#f07a66}
.footer-links{right:107px;top:24px;font-size:11px;color:var(--white);display:flex}
.footer-links span{padding:0 10px;border-left:1px solid #bbb;line-height:12px}
.footer-links span:first-child{border-left:none}
.footer-links span:last-child{padding-right:0}
</style>
</head>
<body>
<div class="page">

  <header>
    <div class="abs brand-mark"></div>
    <div class="abs brand-name">Reed Calloway</div>
    <div class="abs brand-tag">martial arts</div>
    <div class="abs social" style="left:746px"></div>
    <div class="abs social" style="left:779px"></div>
    <div class="abs social" style="left:811px"></div>
    <div class="abs social" style="left:844px"></div>
  </header>

  <nav class="abs nav">
    <ul>
      <li style="width:83px">Home</li>
      <li style="width:105px">About Us</li>
      <li style="width:162px">Monthly Workout</li>
      <li style="width:100px">Gallery</li>
      <li style="width:100px">Archives</li>
      <li style="width:106px">Sponsors</li>
      <li style="width:106px">Contact Us</li>
    </ul>
  </nav>

  <section class="abs hero">
    <div class="abs hero-photo" role="img" aria-label="Young student in a white uniform and black belt performing a flying kick"></div>
    <svg class="abs hero-arrow" style="left:64px" viewBox="0 0 31 31"><circle cx="15.5" cy="15.5" r="15.5" fill="#fff"/><path d="M22 15.5H10M15 9.5l-6 6 6 6" stroke="#e3604f" stroke-width="3.2" fill="none" stroke-linecap="round" stroke-linejoin="round"/></svg>
    <svg class="abs hero-arrow" style="left:887px" viewBox="0 0 31 31"><circle cx="15.5" cy="15.5" r="15.5" fill="#fff"/><path d="M9 15.5h12M16 9.5l6 6-6 6" stroke="#e3604f" stroke-width="3.2" fill="none" stroke-linecap="round" stroke-linejoin="round"/></svg>
    <h1 class="abs hero-title" style="font-weight:400">Effective Self Defence Skills</h1>
    <p class="abs hero-text">Masagni dolores eoquie voluptate msequciunt. Niquerro quisquam estqui dolorem ipsumquia dolor sitamet cone tase adipisci unumquam eius.</p>
    <div class="abs hero-btn">Find Out More</div>
  </section>

  <section>
    <h2 class="abs welcome-title" style="font-weight:400">WELCOME!</h2>
    <p class="abs welcome-lead">Adipisci unumquam eius, basmodi tempra iduntut laboreas dolor.</p>
    <p class="abs welcome-body">Masagni dolores eoquie voluptate msequciunt. Niquerro quisquam estqui dolorem ipsumquia dolor sitamet conetase adipisci unumquam eius. Basmodi tempora idunt, ut laboreas dolorema gnam aliquam quaerat ptatem. Munim ad minim eniamagse quis nostrum.</p>
    <div class="abs read-more">Read More
      <svg width="11" height="11" viewBox="0 0 11 11"><circle cx="5.5" cy="5.5" r="5.5" fill="#e3604f"/><path d="M4.3 3l3 2.5-3 2.5z" fill="#fff"/></svg>
    </div>

    <h2 class="abs video-title" style="font-weight:400">Watch Our Video’s</h2>
    <div class="abs video-frame" role="img" aria-label="Close-up of students in white uniforms with black belts in a training hall"></div>
    <svg class="abs play" viewBox="0 0 58 58"><circle cx="29" cy="29" r="28" fill="#d8d8d8" stroke="#f2f2f2" stroke-width="2"/><circle cx="29" cy="29" r="22" fill="#ececec"/><path d="M24 18l13 11-13 11z" fill="none" stroke="#555" stroke-width="2.4" stroke-linejoin="round"/></svg>
    <p class="abs video-caption">Niquerro quisquam estqui dolorem ipsumquia dolor sitamet conetase adipisci</p>

    <div class="abs signup">
      <div class="abs signup-head">Sign Up for Monthly Updates</div>
      <div class="abs field" style="top:52px">User Name..</div>
      <div class="abs field" style="top:86px">Enter your Email...</div>
      <div class="abs field" style="top:120px;height:54px;left:10px;width:218px">Message...</div>
      <div class="abs signup-btn">SIGN UP</div>
    </div>
  </section>

  <section class="abs gallery">
    <h2 class="abs gallery-title" style="font-weight:400">Our Gallery</h2>
    <svg class="abs gallery-next" viewBox="0 0 23 23"><circle cx="11.5" cy="11.5" r="11" fill="#f4f4f4" stroke="#cfcfcf"/><path d="M9.5 7l4.5 4.5-4.5 4.5" stroke="#444" stroke-width="2" fill="none" stroke-linecap="round"/></svg>
    <div class="abs thumb" style="left:107px;width:240px"><div role="img" aria-label="Two sparring students in protective gear in a bright gym" style="background:linear-gradient(90deg,#c9c3bd,#e6e2df 50%,#d6c9c6)"></div></div>
    <div class="abs thumb" style="left:367px;width:243px"><div role="img" aria-label="Group of students practising side kicks in a dojo" style="background:linear-gradient(90deg,#8e8c93,#b9b2ad 50%,#d9c15a)"></div></div>
    <div class="abs thumb" style="left:627px;width:242px"><div role="img" aria-label="Three women in white practising forms in a forest" style="background:linear-gradient(90deg,#4d5a3c,#8a8f74 50%,#5c5a3f)"></div></div>
  </section>

  <footer class="abs footer">
    <p class="abs footer-copy">(c) 2013. <span>Reed Calloway</span>. All Right Reserved.<br>Privacy Policy.</p>
    <div class="abs footer-links"><span>Home</span><span>Archives</span><span>Site map</span><span>Contact</span></div>
  </footer>

</div>
</body>
</html>
```